RTV Engineering Business Card Design

We’re looking for an elegant, clean, and timeless business card design that communicates experience, capability, and reliability.

RTV Engineering was established in 1995 , we are a Government Contracting company providing Professional Services to the Department of Harbor Affairs, Frontier Resilience and the Signals Consortium. Our capabilities include: Acquisition & Program Management; Intelligence & Security Operations; Cyber, IT & Network Operations; Lifecycle Logistics & Asset Readiness; C5ISR Systems Engineering & Sustainment.

We want the card to reflect a straightforward, confident approach to business. The design should feel polished and professional without being flashy or overly corporate.

Design Direction
Clean, sophisticated, and uncluttered
Elegant but understated
Strong typography and thoughtful spacing
A timeless aesthetic rather than something overly trendy
Confident and established, with a sense of substance
Easy to read and practical in a real-world business setting

The overall impression should be: “These are experienced professionals who know what they’re doing, do what they say, and can be relied upon.”

We’re open to creative interpretations. The finished card should feel distinctive through its typography, proportions, layout, and attention to detail rather than through excessive graphics or visual effects.

We’re looking for a design that would make a potential client immediately feel that they’re dealing with a capable, trustworthy, and established company.

Company Colors: Navy and Gold/Yellow (but you do not need to use these colors on the card)
Company Name: RTV Engineering Associates, Inc. (known as RTV Engineering)
Website: rtvengineering-hq.example
Company Logo: Navy & Gold (other variations attached)

```html
<!DOCTYPE html>
<html lang="en">
<head>
<meta charset="utf-8">
<title>RTV Engineering – Business Card</title>
<link href="https://fonts.googleapis.com/css2?family=Poppins:wght@400;500;700;800&display=swap" rel="stylesheet">
<style>
  :root {
    --navy: #202c5e;
    --gold: #ffe14f;
    --white: #ffffff;
    --stage: #2a2a2c;
    --card-w: 660px;
    --card-h: 377px;
  }
  * { margin: 0; padding: 0; box-sizing: border-box; }
  html, body {
    width: 1200px; height: 880px; overflow: hidden;
    background: var(--stage);
    font-family: "Poppins", sans-serif;
  }
  .stage {
    width: 1200px; height: 880px;
    display: flex; flex-direction: column;
    align-items: center; justify-content: center; gap: 40px;
  }
  .card {
    position: relative;
    width: var(--card-w); height: var(--card-h);
    background: var(--white);
    border-radius: 24px;
    overflow: hidden;
  }
  .card-art { position: absolute; inset: 0; }

  .wordmark {
    position: absolute;
    color: var(--navy);
    font-weight: 800;
    letter-spacing: -0.5px;
    white-space: nowrap;
  }
  .card-front .wordmark {
    left: 0; right: 0; top: 50%;
    transform: translateY(-50%);
    text-align: center;
    font-size: 54px;
  }
  .card-back .wordmark {
    left: 46px; top: 118px;
    font-size: 34px;
  }

  .person {
    position: absolute; right: 42px; top: 28px;
    text-align: right; color: var(--navy);
  }
  .person-name { font-weight: 700; font-size: 19px; letter-spacing: 0.3px; line-height: 1.15; }
  .person-role { font-weight: 400; font-size: 13px; letter-spacing: 0.8px; line-height: 1.3; }

  .contact {
    position: absolute; right: 34px; top: 160px;
    text-align: right; color: var(--white);
    font-size: 12.5px; line-height: 1.45;
  }
  .contact-address { margin-bottom: 12px; padding-right: 30px; }
  .contact-row {
    display: flex; align-items: center; justify-content: flex-end; gap: 8px;
  }
  .contact-icon { width: 20px; height: 20px; flex: none; }
</style>
</head>
<body>
<main class="stage">

  <section class="card card-front" aria-label="Business card front">
    <span class="wordmark">RTV Engineering</span>
  </section>

  <section class="card card-back" aria-label="Business card back">
    <svg class="card-art" viewBox="0 0 660 377" width="660" height="377" aria-hidden="true">
      <path class="gold-sweep" fill="var(--gold)"
            d="M0 282 C190 280 335 225 392 128 C372 240 215 310 0 318 Z"/>
      <path class="navy-wave" fill="var(--navy)"
            d="M0 377 L0 330 C190 328 330 262 405 185 C465 122 545 100 660 96 L660 377 Z"/>
      <path class="wave-gap" fill="none" stroke="var(--white)" stroke-width="6"
            d="M110 356 C290 336 385 252 428 190 C470 136 530 112 620 104"/>
    </svg>

    <span class="wordmark">RTV Engineering</span>

    <div class="person">
      <p class="person-name">MARA QUELL</p>
      <p class="person-role">Manager</p>
    </div>

    <div class="contact">
      <p class="contact-address">4120 Harrow Lane<br>Suite 310, Brackenridge<br>VA 23999</p>
      <p class="contact-row">555-014-2270
        <svg class="contact-icon" viewBox="0 0 20 20"><circle cx="10" cy="10" r="9" fill="none" stroke="var(--gold)" stroke-width="1.4"/><rect x="7" y="5" width="6" height="10" rx="1" fill="none" stroke="var(--gold)" stroke-width="1.3"/></svg>
      </p>
      <p class="contact-row">contact@mailbox.example
        <svg class="contact-icon" viewBox="0 0 20 20"><circle cx="10" cy="10" r="9" fill="none" stroke="var(--gold)" stroke-width="1.4"/><rect x="5.5" y="6.5" width="9" height="7" fill="none" stroke="var(--gold)" stroke-width="1.3"/><path d="M5.5 6.5 L10 10.5 L14.5 6.5" fill="none" stroke="var(--gold)" stroke-width="1.3"/></svg>
      </p>
      <p class="contact-row">www.rtvengineering-hq.example
        <svg class="contact-icon" viewBox="0 0 20 20"><circle cx="10" cy="10" r="9" fill="none" stroke="var(--gold)" stroke-width="1.4"/><circle cx="10" cy="10" r="5" fill="none" stroke="var(--gold)" stroke-width="1.2"/><path d="M5 10 H15 M10 5 C8 7.5 8 12.5 10 15 M10 5 C12 7.5 12 12.5 10 15" fill="none" stroke="var(--gold)" stroke-width="1"/></svg>
      </p>
    </div>
  </section>

</main>
</body>
</html>
```